Painting Contractor Business Card Design

We are looking for a cool, bold, modern, polished, business card design. We are a high-end residential painting contractor. Please incorporate our logo and keep with our green/black color scheme. We are interested in seeing 2-sided and 1-sided options. Thank you very much!

Industry/Entity Type

Business

Contact Information for Business Card

Info for the card:
Dale Ormsby
mobile 206-555-0193
email dale@tallowbrookpainting.net
web www.tallowbrookpainting.net

```html
<!DOCTYPE html>
<html lang="en">
<head>
<meta charset="utf-8">
<title>Tallowbrook Painting – Business Card</title>
<link rel="stylesheet" href="https://fonts.googleapis.com/css2?family=Lato:wght@400;700;900&display=swap">
<style>
  :root {
    --backdrop: #161616;
    --card: #1d1d1f;
    --card-edge: #2a2a2c;
    --ink: #f2f2f2;
    --ink-soft: #d6d6d6;
    --green: #3fae49;
    --band-start: #1fa3e0;
    --band-mid: #3cc3a0;
    --band-end: #d9d93a;
  }
  * { box-sizing: border-box; margin: 0; padding: 0; }
  html, body {
    width: 1200px; height: 864px; overflow: hidden;
    background: var(--backdrop);
    font-family: "Lato", Arial, sans-serif;
  }
  .sheet {
    position: relative; width: 1200px; height: 864px;
    display: flex; align-items: center; justify-content: center; gap: 60px;
  }
  .card {
    position: relative; width: 520px; height: 297px;
    background: var(--card);
    border: 1px solid var(--card-edge);
    border-radius: 18px;
    overflow: hidden;
  }
  /* contact side */
  .edge-band {
    position: absolute; height: 9px;
    background: linear-gradient(90deg, var(--band-start), var(--band-mid), var(--band-end));
  }
  .edge-band--top { top: 0; left: 270px; width: 180px; border-radius: 0 0 6px 6px; }
  .edge-band--bottom { bottom: 0; left: 170px; width: 180px; border-radius: 6px 6px 0 0; }
  .contact {
    position: absolute; left: 48px; top: 82px;
  }
  .contact__name {
    color: var(--ink); font-weight: 900; font-size: 19px; letter-spacing: 0.5px;
    text-transform: uppercase;
  }
  .contact__role {
    color: var(--green); font-size: 13px; letter-spacing: 0.5px; margin-top: 2px;
    text-transform: uppercase;
  }
  .contact__list { list-style: none; margin-top: 18px; }
  .contact__item {
    display: flex; align-items: center; gap: 9px;
    color: var(--ink-soft); font-size: 13.5px; line-height: 21px;
  }
  .contact__icon { width: 12px; height: 12px; flex: none; }
  .divider {
    position: absolute; left: 268px; top: 78px; width: 1px; height: 140px;
    background: var(--green);
  }
  .mark {
    position: absolute; left: 290px; right: 20px; top: 0; bottom: 0;
    display: flex; align-items: center; justify-content: center; gap: 10px;
  }
  .mark__square { width: 14px; height: 14px; background: var(--green); flex: none; }
  .mark__name {
    color: var(--ink); font-weight: 900; font-size: 17px; letter-spacing: 0.5px;
    text-transform: uppercase; line-height: 1.25;
  }
  /* brand side */
  .brand {
    position: absolute; inset: 0;
    display: flex; flex-direction: column; align-items: center; justify-content: center;
  }
  .brand__lockup { display: flex; align-items: center; gap: 12px; }
  .brand__square { width: 20px; height: 20px; background: var(--green); }
  .brand__name {
    color: var(--ink); font-weight: 900; font-size: 28px; letter-spacing: 0.5px;
    text-transform: uppercase;
  }
  .brand__web {
    margin-top: 22px; color: var(--green); font-size: 15px; letter-spacing: 0.3px;
  }
</style>
</head>
<body>
<main class="sheet">
  <section class="card card--contact" aria-label="Card front with contact details">
    <div class="edge-band edge-band--top"></div>
    <div class="edge-band edge-band--bottom"></div>
    <div class="contact">
      <h1 class="contact__name">Dale Ormsby</h1>
      <p class="contact__role">Manager</p>
      <ul class="contact__list">
        <li class="contact__item">
          <svg class="contact__icon" viewBox="0 0 12 12" aria-hidden="true"><path fill="#3fae49" d="M2.5 1h2l1 2.6-1.3 1a6 6 0 0 0 3.2 3.2l1-1.3L11 7.5v2A1.5 1.5 0 0 1 9.5 11 8.5 8.5 0 0 1 1 2.5 1.5 1.5 0 0 1 2.5 1z"/></svg>
          206-555-0193
        </li>
        <li class="contact__item">
          <svg class="contact__icon" viewBox="0 0 12 12" aria-hidden="true"><rect x="0.5" y="2" width="11" height="8" rx="1" fill="#3fae49"/><path d="M1 2.6l5 4 5-4" fill="none" stroke="#1d1d1f" stroke-width="1.1"/></svg>
          dale@tallowbrookpainting.net
        </li>
        <li class="contact__item">
          <svg class="contact__icon" viewBox="0 0 12 12" aria-hidden="true"><circle cx="6" cy="6" r="5.3" fill="#3fae49"/><path d="M0.8 6h10.4M6 0.8c-2.6 2.8-2.6 7.6 0 10.4M6 0.8c2.6 2.8 2.6 7.6 0 10.4" fill="none" stroke="#1d1d1f" stroke-width="0.9"/></svg>
          www.tallowbrookpainting.net
        </li>
      </ul>
    </div>
    <div class="divider"></div>
    <div class="mark">
      <span class="mark__square"></span>
      <span class="mark__name">Tallowbrook<br>Painting</span>
    </div>
  </section>

  <section class="card card--brand" aria-label="Card back with company name">
    <div class="brand">
      <div class="brand__lockup">
        <span class="brand__square"></span>
        <span class="brand__name">Tallowbrook Painting</span>
      </div>
      <p class="brand__web">www.tallowbrookpainting.net</p>
    </div>
  </section>
</main>
</body>
</html>
```